Want to fly? Flight school needs a roll up

Hello designers

We are a small aviation club with around 100 members. We love flying and therefore offer free flight lessons for young people at our glider flight school.
The young people only have to pay a flat rate of €300 for the aircraft until their first solo flight.
To advertise the flight school we now need a roll up banner measuring 85cm x 200cm. You can find the data sheet for the banner in the appendix.
Content of the roll up banner:
Advertising for our flight school so that we can attract new members
The banner should be designed in our club colors blue/white
The banner is aimed at all people who want to get a glider license
A great offer for young people up to the age of 25 should be placed on the banner with a reference to the text “Offer only applies to people up to the age of 25. Included in the flat rate of €300 is training on the glider up to the first "solo flight"
The banner is intended to advertise training with a glider. Therefore the wish would be for a glider to be depicted

Here is a link to our current homepage

https://www.lsg-tarnhofen.de/

https://www.vidoplex.example/watch?v=K8p2Qz4LmXc

Target Market(s)

Young people from 14 years to 30 years

Colors
0054AA
0677BA
7BADD7
CADEEF
E8F1F8

Requirements
Nice to have
• Glider / club logo
Should not have
• Too much text

```html
<!DOCTYPE html>
<html lang="de">
<head>
<meta charset="utf-8">
<title>Jetzt Pilot werden – Roll-up</title>
<link rel="stylesheet" href="https://fonts.googleapis.com/css2?family=Bebas+Neue&family=Montserrat:wght@300;500;700;800&display=swap">
<style>
  :root {
    --page-bg: #eef2f6;
    --banner-white: #f7f8fa;
    --club-blue: #10198f;
    --deep-navy: #0a1248;
    --footer-grey: #58595d;
    --text-white: #ffffff;
    --url-grey: #e8e8ea;
    --sky-dark: #2d3c58;
    --sky-mid: #8a97aa;
    --cloud-light: #e4e7ec;
  }
  html, body {
    margin: 0;
    padding: 0;
    width: 1200px;
    height: 900px;
    overflow: hidden;
    background: var(--page-bg);
  }
  .rollup {
    position: absolute;
    left: 415px;
    top: 21px;
    width: 370px;
    height: 858px;
    overflow: hidden;
    box-shadow: 0 6px 24px rgba(20, 30, 60, 0.18);
  }
  .rollup-shapes {
    position: absolute;
    inset: 0;
    width: 370px;
    height: 858px;
    display: block;
  }
  .club-mark {
    position: absolute;
    left: 0;
    right: 0;
    top: 40px;
    display: flex;
    flex-direction: column;
    align-items: center;
    gap: 8px;
  }
  .club-mark-circle {
    width: 52px;
    height: 52px;
    border-radius: 50%;
    border: 3px solid var(--club-blue);
    box-sizing: border-box;
  }
  .club-name {
    font-family: "Montserrat", sans-serif;
    font-weight: 700;
    font-size: 13px;
    color: var(--club-blue);
    letter-spacing: 0.2px;
  }
  .headline {
    position: absolute;
    left: 0;
    right: 0;
    top: 194px;
    margin: 0;
    text-align: center;
    font-family: "Bebas Neue", sans-serif;
    font-weight: 400;
    font-size: 46px;
    line-height: 1;
    color: var(--text-white);
    letter-spacing: 0.3px;
  }
  .offer {
    position: absolute;
    left: 0;
    right: 0;
    top: 249px;
    margin: 0;
    text-align: center;
    font-family: "Montserrat", sans-serif;
    font-weight: 500;
    font-size: 23px;
    line-height: 29px;
    color: var(--text-white);
    letter-spacing: 0.6px;
  }
  .offer-price {
    font-weight: 800;
  }
  .website {
    position: absolute;
    left: 0;
    right: 0;
    top: 785px;
    margin: 0;
    text-align: center;
    font-family: "Montserrat", sans-serif;
    font-weight: 300;
    font-size: 15px;
    color: var(--url-grey);
    letter-spacing: 0.8px;
  }
  .website-domain {
    font-weight: 700;
  }
</style>
</head>
<body>
  <section class="rollup">
    <svg class="rollup-shapes" viewBox="0 0 470 1090" preserveAspectRatio="none">
      <defs>
        <linearGradient id="sky-clouds" x1="0" y1="0" x2="0.3" y2="1">
          <stop offset="0" stop-color="var(--sky-dark)"/>
          <stop offset="0.35" stop-color="var(--sky-mid)"/>
          <stop offset="0.75" stop-color="var(--cloud-light)"/>
          <stop offset="1" stop-color="#f4f5f7"/>
        </linearGradient>
      </defs>
      <rect class="banner-base" x="0" y="0" width="470" height="1090" fill="var(--banner-white)"/>
      <path class="navy-swoosh" d="M0,198 Q200,262 470,122 L470,152 Q230,258 0,226 Z" fill="var(--deep-navy)"/>
      <path class="blue-band" d="M0,226 Q230,258 470,152 L470,520 L0,520 Z" fill="var(--club-blue)"/>
      <rect class="footer-band" x="0" y="820" width="470" height="270" fill="var(--footer-grey)"/>
      <path class="photo-frame" d="M0,418 Q190,382 470,468 L470,912 Q320,1000 150,968 Q40,940 0,840 Z" fill="var(--text-white)"/>
      <path class="photo-area" role="img" aria-label="Photo: aircraft wing flying above bright cumulus clouds"
            d="M0,427 Q190,392 470,478 L470,904 Q320,990 152,958 Q44,930 0,832 Z" fill="url(#sky-clouds)"/>
    </svg>

    <div class="club-mark">
      <div class="club-mark-circle"></div>
      <span class="club-name">Luftsportgruppe Tarnhofen e.V.</span>
    </div>

    <h1 class="headline">Jetzt Pilot werden</h1>
    <p class="offer"><span class="offer-price">300 €</span> BIS ZUM ERSTEN<br>ALLEINFLUG</p>

    <p class="website">www.<span class="website-domain">LSG-TARNHOFEN</span>.de</p>
  </section>
</body>
</html>
```